KVT Business Cards

We require business cards for our business. We would like a matte black back to the card, with our logo centred in the middle. The front side of the card is open to design.

Target Market(s)

Clients looking for legal services (professional)

Industry/Entity Type

Legal

Contact Information for Business Card

Boris Telemark
Partner
Mobile: 0438 715 642
Email: boris@kvtlaw.co
Website: www.kvtlaw.co
Level 3, 118 Wexbury Street
Sydney NSW 2000

Font styles to use
Other font styles liked:
• Avenir

Colors
f04a50
ffffff
1b1b1b

Requirements
Must have
• Black back with logo included in the centre of the card.
• Our font is Avenir.

```html
<!DOCTYPE html>
<html lang="en">
<head>
<meta charset="utf-8">
<title>KVT Legal Business Cards</title>
<link rel="stylesheet" href="https://fonts.googleapis.com/css2?family=Mulish:wght@400;600;700&display=swap">
<style>
  :root {
    --backdrop: #2b2b2b;
    --card-dark: #1f1a1e;
    --card-light: #f4f4f3;
    --accent: #b3254b;
    --ink: #262326;
    --white: #ffffff;
    --muted-white: #e9e6e8;
  }
  * { margin: 0; padding: 0; box-sizing: border-box; }
  html, body {
    width: 1200px;
    height: 785px;
    overflow: hidden;
    background: var(--backdrop);
    font-family: "Mulish", "Avenir", sans-serif;
  }
  .stage {
    position: relative;
    width: 1200px;
    height: 785px;
  }
  .card {
    position: absolute;
    top: 248px;
    width: 450px;
    height: 288px;
    box-shadow: 0 10px 24px rgba(0, 0, 0, 0.45);
  }
  .card--back {
    left: 119px;
    background: var(--card-dark);
  }
  .card--front {
    left: 631px;
    background: var(--card-light);
    color: var(--ink);
  }

  /* Wordmark */
  .wordmark {
    position: absolute;
    display: flex;
    align-items: center;
    gap: 14px;
  }
  .wordmark__square {
    width: 22px;
    height: 22px;
    background: var(--accent);
  }
  .wordmark__name {
    font-weight: 700;
    letter-spacing: 0.02em;
    line-height: 1;
  }
  .card--back .wordmark {
    left: 50%;
    top: 50%;
    transform: translate(-50%, -50%);
  }
  .card--back .wordmark__name {
    font-size: 34px;
    color: var(--muted-white);
  }
  .card--front .wordmark {
    right: 30px;
    top: 72px;
  }
  .card--front .wordmark__square {
    width: 18px;
    height: 18px;
  }
  .card--front .wordmark__name {
    font-size: 24px;
    color: var(--ink);
  }

  /* Holder */
  .holder {
    position: absolute;
    left: 29px;
    top: 68px;
  }
  .holder__name {
    font-size: 13px;
    font-weight: 600;
    color: var(--accent);
  }
  .holder__role {
    margin-top: 5px;
    font-size: 13px;
  }
  .holder__rule {
    margin-top: 6px;
    width: 46px;
    height: 3px;
    background: var(--ink);
  }

  /* Contact */
  .contact, .address {
    position: absolute;
    top: 216px;
    font-size: 13px;
    line-height: 19px;
    list-style: none;
  }
  .contact { left: 29px; }
  .contact__web { color: var(--accent); }
  .address { left: 255px; font-style: normal; }
</style>
</head>
<body>
  <main class="stage">
    <section class="card card--back" aria-label="Card back">
      <div class="wordmark">
        <span class="wordmark__square"></span>
        <span class="wordmark__name">KVT LEGAL</span>
      </div>
    </section>

    <section class="card card--front" aria-label="Card front">
      <div class="holder">
        <p class="holder__name">Boris Telemark</p>
        <p class="holder__role">Partner</p>
        <div class="holder__rule"></div>
      </div>

      <div class="wordmark">
        <span class="wordmark__square"></span>
        <span class="wordmark__name">KVT LEGAL</span>
      </div>

      <ul class="contact">
        <li>0438 715 642</li>
        <li>boris@kvtlaw.co</li>
        <li class="contact__web">www.kvtlaw.co</li>
      </ul>

      <address class="address">
        Level 3, 118 Wexbury St<br>
        Sydney<br>
        NSW 2000
      </address>
    </section>
  </main>
</body>
</html>
```